New Business Card Design Project

Updated business card design. I am moving towards more coaching of, for the most part women, who are searching for more in their lives. I am an intuitive healer, homeopath and nutritionist but also an author and motivational speaker. Int the past I have included my photo on the card but that is not essential. My book is called the Brilliance of Saffron - Reclaiming the Shade of Your Spirit so my colours are typically magenta.
Target Market(s)
Women - 35 - 60 considering improving their health. However, I am also a professional speaker with a target audience including corporate and conferences.
Industry/Entity Type
Health And Wellness
Contact Information for Business Card
Lucinda Parvell, Hom, RHN, BA
www.lucindaparvell.com
lucinda@lucindaparvell.com
519-362-7015
Facebook, instagram and twitter logos
Look and feel
Each slider illustrates characteristics of the customer's brand and the style your logo design should communicate.

```html
<!DOCTYPE html>
<html lang="en">
<head>
<meta charset="utf-8">
<title>Lucinda Parvell – Business Card</title>
<link rel="stylesheet" href="https://fonts.googleapis.com/css2?family=Cutive&display=swap">
<style>
  :root {
    --backdrop: #dcdcdc;
    --card: #efeeec;
    --magenta: #d61c6c;
    --magenta-deep: #c01560;
    --purple: #8e3f8f;
    --lavender: #b98bbb;
    --ink: #2e2a2c;
    --photo-dark: #3f4a38;
    --photo-light: #c9b9a6;
  }
  * { margin: 0; padding: 0; box-sizing: border-box; }
  html, body { width: 1200px; height: 1103px; overflow: hidden; background: var(--backdrop); }
  .stage { position: relative; width: 1200px; height: 1103px; }
  .card {
    position: absolute; left: 75px; top: 251px; width: 1050px; height: 600px;
    background: var(--card); overflow: hidden;
    box-shadow: 0 18px 40px rgba(0,0,0,0.18);
  }
  .card-art { position: absolute; inset: 0; }
  .brand {
    position: absolute; left: 462px; top: 66px;
    font-family: "Cutive", serif; font-size: 50px; font-weight: 400;
    color: var(--ink); letter-spacing: -1px; white-space: nowrap;
  }
  .contact {
    position: absolute; left: 465px; top: 188px;
    font-family: "Cutive", serif; color: var(--ink); list-style: none;
  }
  .contact-name { font-size: 25px; font-variant: small-caps; letter-spacing: 1px; margin-bottom: 14px; white-space: nowrap; }
  .contact-name .credentials { font-size: 19px; font-variant: normal; margin-left: 14px; letter-spacing: 0; }
  .contact-item { display: flex; align-items: center; gap: 16px; font-size: 25px; margin-bottom: 10px; white-space: nowrap; }
  .contact-item svg { width: 22px; height: 22px; flex: none; }
  .social { position: absolute; left: 545px; top: 508px; display: flex; gap: 28px; }
  .social-dot { width: 46px; height: 46px; border-radius: 50%; background: var(--purple); opacity: .85; }
</style>
</head>
<body>
<main class="stage">
  <article class="card">
    <svg class="card-art" viewBox="0 0 1050 600" width="1050" height="600">
      <defs>
        <linearGradient id="photoTone" x1="0" y1="0" x2="1" y2="0">
          <stop offset="0" stop-color="#3f4a38"/>
          <stop offset="0.55" stop-color="#6b5a52"/>
          <stop offset="1" stop-color="#c9b9a6"/>
        </linearGradient>
      </defs>
      <path role="img" aria-label="Portrait photograph of the coach standing by a brick wall"
            d="M0 30 L250 30 Q370 40 395 190 L395 600 L0 600 Z" fill="url(#photoTone)"/>
      <path class="wave-lavender" d="M0 520 Q420 380 1050 340 L1050 600 L0 600 Z" fill="#b98bbb" opacity=".85"/>
      <path class="wave-purple" d="M0 545 Q420 410 1050 375 L1050 600 L0 600 Z" fill="#8e3f8f" opacity=".7"/>
      <path class="wave-magenta" d="M0 565 Q420 440 1050 400 L1050 600 L0 600 Z" fill="#d61c6c"/>
      <path class="wave-shade" d="M0 600 Q500 520 1050 470 L1050 600 Z" fill="#c01560" opacity=".5"/>
    </svg>

    <div class="brand">Lucinda Parvell</div>

    <ul class="contact">
      <li class="contact-name">Lucinda Parvell<span class="credentials">Hom, RHN, BA</span></li>
      <li class="contact-item">
        <svg viewBox="0 0 24 24" fill="none" stroke="#8e3f8f" stroke-width="2">
          <circle cx="12" cy="12" r="10"/><ellipse cx="12" cy="12" rx="4" ry="10"/><line x1="2" y1="12" x2="22" y2="12"/>
        </svg>
        www.lucindaparvell.com
      </li>
      <li class="contact-item">
        <svg viewBox="0 0 24 24" fill="none" stroke="#8e3f8f" stroke-width="2">
          <rect x="2" y="5" width="20" height="14"/><polyline points="2,5 12,13 22,5"/>
        </svg>
        lucinda@lucindaparvell.com
      </li>
      <li class="contact-item">
        <svg viewBox="0 0 24 24" fill="#8e3f8f">
          <path d="M6.6 10.8a15 15 0 0 0 6.6 6.6l2.2-2.2a1 1 0 0 1 1-.25 11.4 11.4 0 0 0 3.6.57 1 1 0 0 1 1 1V20a1 1 0 0 1-1 1A17 17 0 0 1 3 4a1 1 0 0 1 1-1h3.5a1 1 0 0 1 1 1c0 1.25.2 2.45.57 3.57a1 1 0 0 1-.25 1z"/>
        </svg>
        519-362-7015
      </li>
    </ul>

    <div class="social" aria-label="Social media links">
      <span class="social-dot"></span><span class="social-dot"></span><span class="social-dot"></span>
    </div>
  </article>
</main>
</body>
</html>
```